I own a small business whose primary function is Professional Fashion and Commercial Photography and has a secondary function of Talent Management of Models/Actors. I've used NorthPress in the past to print my own design, but I'd like something a bit more topical, fresh and done by an artist instead of a photographer (me).

My company logo is included with a few selected horizontal (landscape) photos of some of my models--I'd like to use a single model photo as the background for the entire card, either in color or converted to black and white, at opacity enough to see the photo but not too much to obscure any text or the company logo, or use a photo as a share of the card (not the entire background), or use all the three models on the card in some manor... Our company colors are white, black, grey-silver and red.

Industry/Entity Type

Small Business

Contact Information for Business Card

Daniel Hartwell, Owner
KTL Productions
PO Box 7713
Brattleboro VT 05917-7713
(860) 555-0147
dan@ktlproductions-example,.com

```html
<!DOCTYPE html>
<html lang="en">
<head>
<meta charset="UTF-8">
<title>KTL Productions — Business Card</title>
<link href="https://fonts.googleapis.com/css2?family=Open+Sans:wght@400;600;700&display=swap" rel="stylesheet">
<style>
  :root {
    --page-bg: #8f8f8f;
    --brand-red: #e8432e;
    --brand-black: #070707;
    --brand-white: #ffffff;
    --brand-grey: #6e6e6e;
    --band-white: rgba(255, 255, 255, 0.72);
    --box-fill: #1c1c1c;
  }
  * { box-sizing: border-box; margin: 0; padding: 0; }
  html, body {
    width: 1200px;
    height: 1000px;
    overflow: hidden;
    background: var(--page-bg);
    font-family: "Open Sans", Arial, sans-serif;
  }
  .card {
    position: absolute;
    left: 190px;
    width: 820px;
    height: 460px;
    overflow: hidden;
    box-shadow: 0 6px 18px rgba(0, 0, 0, 0.25);
  }

  /* Front side: model photography */
  .card-front {
    top: 30px;
    background: var(--brand-white);
    border-top: 16px solid var(--brand-red);
    border-bottom: 16px solid var(--brand-red);
  }
  .photo-strip {
    position: absolute;
    inset: 0;
    display: flex;
  }
  .photo { height: 100%; }
  .photo-model-one {
    width: 33%;
    background: linear-gradient(160deg, #b8312a 0%, #c94738 55%, #e0a58c 100%);
  }
  .photo-model-two {
    width: 34%;
    background: linear-gradient(180deg, #2a2422 0%, #7a5a4a 45%, #c98a8a 100%);
  }
  .photo-model-three {
    width: 33%;
    background: linear-gradient(170deg, #6f8f3a 0%, #b58a6e 45%, #c2352f 100%);
  }
  .brand-band {
    position: absolute;
    left: 0;
    right: 0;
    top: 232px;
    height: 160px;
    background: var(--band-white);
  }
  .front-brand {
    position: absolute;
    left: 300px;
    top: 270px;
    display: flex;
    align-items: center;
    gap: 14px;
  }
  .brand-mark {
    width: 40px;
    height: 40px;
    flex: none;
    background: var(--brand-red);
  }
  .brand-name {
    font-weight: 700;
    font-size: 44px;
    letter-spacing: 1px;
    white-space: nowrap;
    color: var(--brand-black);
  }
  .front-brand .brand-name { color: var(--brand-grey); }

  /* Back side: contact details */
  .card-back {
    top: 515px;
    background: var(--brand-black);
    border-top: 20px solid var(--brand-red);
    border-bottom: 20px solid var(--brand-red);
  }
  .identity {
    position: absolute;
    left: 26px;
    top: 58px;
    width: 360px;
    text-align: center;
  }
  .logo-panel {
    display: flex;
    align-items: center;
    justify-content: center;
    gap: 12px;
    width: 340px;
    height: 100px;
    margin: 0 auto 18px;
    padding: 0 16px;
    background: var(--brand-white);
  }
  .logo-panel .brand-mark { width: 28px; height: 28px; }
  .logo-panel .brand-name { font-size: 28px; letter-spacing: 0.5px; }
  .person-name {
    font-size: 27px;
    font-weight: 700;
    letter-spacing: -0.5px;
    color: var(--brand-red);
    line-height: 1.1;
  }
  .person-role {
    font-size: 15px;
    color: var(--brand-white);
    margin-bottom: 4px;
  }
  .services {
    font-size: 16px;
    font-weight: 700;
    letter-spacing: -0.3px;
    color: var(--brand-red);
    line-height: 1.2;
  }
  .contact-list {
    position: absolute;
    left: 420px;
    top: 62px;
    width: 370px;
    list-style: none;
  }
  .contact-item {
    display: flex;
    align-items: center;
    gap: 24px;
    height: 86px;
    margin-bottom: 18px;
    padding: 0 24px;
    background: var(--box-fill);
    border: 2px solid var(--brand-red);
    border-radius: 10px;
    color: var(--brand-white);
    font-size: 16px;
    line-height: 1.35;
  }
  .contact-icon {
    width: 24px;
    height: 24px;
    flex: none;
    fill: var(--brand-white);
  }
</style>
</head>
<body>

<section class="card card-front" aria-label="Business card front">
  <div class="photo-strip">
    <div class="photo photo-model-one" role="img" aria-label="Portrait of a young male model in a red sleeveless top against a red backdrop"></div>
    <div class="photo photo-model-two" role="img" aria-label="Portrait of a teenage model with long hair wearing a black cap"></div>
    <div class="photo photo-model-three" role="img" aria-label="Portrait of a young boy model in a red shirt outdoors"></div>
  </div>
  <div class="brand-band"></div>
  <div class="front-brand">
    <span class="brand-mark"></span>
    <span class="brand-name">KTL Productions</span>
  </div>
</section>

<section class="card card-back" aria-label="Business card back">
  <div class="identity">
    <div class="logo-panel">
      <span class="brand-mark"></span>
      <span class="brand-name">KTL Productions</span>
    </div>
    <p class="person-name">DANIEL HARTWELL</p>
    <p class="person-role">Owner</p>
    <p class="services">PRO FASHION &amp; COMMERCIAL PHOTOGRAPHY<br>AND TALENT MANAGEMENT</p>
  </div>

  <ul class="contact-list">
    <li class="contact-item">
      <svg class="contact-icon" viewBox="0 0 24 24" aria-hidden="true">
        <path d="M12 3 2 12h3v9h5v-6h4v6h5v-9h3z"/>
      </svg>
      <span>PO Box 7713<br>Ashcombe VT 05917-7713</span>
    </li>
    <li class="contact-item">
      <svg class="contact-icon" viewBox="0 0 24 24" aria-hidden="true">
        <path d="M3 8c0-2 4-4 9-4s9 2 9 4v2h-4V8.5c-1.5-.6-3-.9-5-.9s-3.5.3-5 .9V10H3z"/>
        <path d="M6 12h12l2 8H4z"/>
      </svg>
      <span>+ (555) 555-0147</span>
    </li>
    <li class="contact-item">
      <svg class="contact-icon" viewBox="0 0 24 24" aria-hidden="true">
        <path d="M2 4h20v13H2zm2 2v9h16V6z"/>
        <path d="M9 18h6v2h3v1H6v-1h3z"/>
      </svg>
      <span>dan@ktlproductions-example,.com</span>
    </li>
  </ul>
</section>

</body>
</html>
```